Modern, Sleek Business Card Design for Corvane Systems

Please create a modern business card, preferably all black with white logo and writing for Corvane Systems, a defense and aerospace company.

Contact Information for Business Card

symbol on one side and name, title, contact info on the other side.

```html
<!DOCTYPE html>
<html lang="en">
<head>
<meta charset="utf-8">
<title>Corvane Systems – Business Card</title>
<link href="https://fonts.googleapis.com/css2?family=Poppins:wght@400;500;600&display=swap" rel="stylesheet">
<style>
  :root {
    --backdrop: #3a3a3a;
    --card-dark: #141414;
    --card-light: #ffffff;
    --ink-dark: #111111;
    --ink-light: #ffffff;
    --rule: #222222;
    --shade-soft: #2a2a2a;
  }
  * { margin: 0; padding: 0; box-sizing: border-box; }
  html, body {
    width: 800px; height: 1200px; overflow: hidden;
    background: var(--backdrop);
    font-family: "Poppins", sans-serif;
  }
  .sheet {
    position: relative; width: 800px; height: 1200px;
    display: flex; flex-direction: column; align-items: center; justify-content: space-around;
    padding: 60px 0;
  }
  .card {
    position: relative; width: 640px; height: 366px;
    border-radius: 6px; overflow: hidden;
    box-shadow: 0 10px 28px rgba(0,0,0,.45);
  }
  .card--front { background: var(--card-dark); color: var(--ink-light); }
  .card--back { background: var(--card-light); color: var(--ink-dark); }

  .brand {
    display: flex; align-items: center; gap: 12px;
    font-weight: 500; letter-spacing: 4px; text-transform: uppercase;
  }
  .brand__mark { width: 16px; height: 16px; background: currentColor; }

  .card--front .brand { position: absolute; left: 48px; top: 44px; font-size: 22px; }
  .front__shade {
    position: absolute; right: 0; bottom: 0; width: 62%; height: 68%;
    background: linear-gradient(135deg, var(--card-dark) 0%, var(--shade-soft) 55%, #6a6a6a 100%);
  }

  .back__identity {
    position: absolute; left: 0; top: 0; width: 57%; height: 100%;
    display: flex; align-items: center; justify-content: center;
  }
  .card--back .brand { font-size: 22px; letter-spacing: 3px; }
  .back__rule {
    position: absolute; left: 57%; top: 42px; bottom: 42px;
    width: 1px; background: var(--rule);
  }
  .back__details { position: absolute; left: 62%; top: 56px; right: 20px; }
  .person__name { font-size: 18px; font-weight: 600; letter-spacing: .5px; }
  .person__title { font-size: 11px; font-weight: 600; letter-spacing: .5px; margin-bottom: 16px; }
  .contact { list-style: none; font-size: 14px; line-height: 1.45; margin-bottom: 14px; }
  .contact li { display: flex; align-items: center; gap: 8px; white-space: nowrap; }
  .contact svg { width: 12px; height: 12px; fill: var(--ink-dark); flex: none; }
  .address { font-size: 12px; line-height: 1.5; font-style: normal; margin-bottom: 8px; }
  .website { font-size: 15px; font-weight: 500; }
</style>
</head>
<body>
<main class="sheet">
  <section class="card card--front" aria-label="Card front">
    <div class="brand"><span class="brand__mark"></span>Corvane Systems</div>
    <div class="front__shade"></div>
  </section>

  <section class="card card--back" aria-label="Card back">
    <div class="back__identity">
      <div class="brand"><span class="brand__mark"></span>Corvane Systems</div>
    </div>
    <div class="back__rule"></div>
    <div class="back__details">
      <p class="person__name">DANIEL MARLOWE</p>
      <p class="person__title">MANAGING DIRECTOR</p>
      <ul class="contact">
        <li><svg viewBox="0 0 24 24" aria-hidden="true"><path d="M6.6 10.8a15.1 15.1 0 006.6 6.6l2.2-2.2c.3-.3.7-.4 1-.2 1.1.4 2.3.6 3.6.6.6 0 1 .4 1 1V20c0 .6-.4 1-1 1A17 17 0 013 4c0-.6.4-1 1-1h3.5c.6 0 1 .4 1 1 0 1.3.2 2.5.6 3.6.1.3 0 .7-.2 1z"/></svg>555 014 22 37</li>
        <li><svg viewBox="0 0 24 24" aria-hidden="true"><path d="M7 1h10a2 2 0 012 2v18a2 2 0 01-2 2H7a2 2 0 01-2-2V3a2 2 0 012-2zm0 3v14h10V4zm5 15.5a1.2 1.2 0 100 2.4 1.2 1.2 0 000-2.4z"/></svg>555 019 40 61</li>
        <li><svg viewBox="0 0 24 24" aria-hidden="true"><path d="M2 5h20v14H2zm2 2v.5l8 5 8-5V7z"/></svg>info@corvane-systems.com</li>
      </ul>
      <address class="address">48 Harbor Lane<br>Millbrook, New York 12545</address>
      <p class="website">www.corvane-systems.com</p>
    </div>
  </section>
</main>
</body>
</html>
```